Website Redesign for Technology Focused Investment Bank

We need a website redesign for a technology and digital media focused investment banking firm. Think modern and forward thinking yet stable and smart. We provide mergers and acquisitions advisory services to our clients. Our target market are CEO's and CFO's (senior executives) that run and operate technology firms.

Larkstone Capital Partners - www.larkstonecapitalpartners.example

We are headquartered in Los Angeles, CA. Please do NOT use the Pemberly marker for anything.

We have the content and can update the photos as well.

We are looking for a "template" website we can update and edit with ease.

A competitive firm's website is: www.brackenhale.example Not sure I like it but I want it to look way better then this one.

Looking for a more modern version. Not too stuffy and conservative, please. Elegant, smart, updated and progressive/modern.
Updates

Color preferences:  Blue's including matching logo color. Grey's. You can add other colors if it flows well and looks clean and nice.

Menu:  Drop Down

Open to platform...please use one that most people can use, is reasonably priced if I need to buy it, and easy to update monthly and sometimes weekly.

Please use this website as a good example of what we are looking for (or similar version of it): www.quelmora.example

Thanks!
Derek P.

We are reviewing all submissions and will select one this week. Thank you everyone for your outstanding and creative designs you have sent us. We really appreciate it.

Thanks for everyone's hard work and creative input into our website design. We really appreciate it!

Target Market(s)

CEO's and CFO's, Entrepreneurs and Board Members of Technology Companies.

Industry/Entity Type

Investment

Font styles to use
Sans Serif

Colors
33a6d7
0492cd
0555a3
3176b5
85abd2
333333
5c5c5c
757575

Requirements
Must have
• Links to social media including Twitter, LinkedIn, Google+, Facebook, etc.

Must try to match logo color
Should not have
• No conservative, old looking colors or background. For example, no green marble look.

```html
<!DOCTYPE html>
<html lang="en">
<head>
<meta charset="utf-8">
<title>Larkstone Capital Partners – Homepage Options</title>
<link href="https://fonts.googleapis.com/css2?family=Open+Sans:wght@300;400;600;700&family=Raleway:wght@300&display=swap" rel="stylesheet">
<style>
:root{
  --blue:#1f6fb8;
  --blue-dark:#0555a3;
  --label-blue:#2f7fc1;
  --ink:#333333;
  --muted:#5c5c5c;
  --soft:#757575;
  --black:#000000;
  --footer:#111111;
  --band:#efefef;
  --rule:#d6d6d6;
  --white:#ffffff;
}
*{margin:0;padding:0;box-sizing:border-box}
html,body{width:1200px;height:900px;overflow:hidden;background:var(--white)}
body{position:relative;font-family:"Open Sans",Arial,sans-serif;color:var(--ink)}

/* option labels */
.option-label{position:absolute;top:450px;font-family:"Raleway",Arial,sans-serif;font-weight:300;font-size:35px;color:var(--label-blue);white-space:nowrap;transform:translate(-50%,-50%) rotate(90deg);letter-spacing:.5px}
.option-label--one{left:36px}
.option-label--two{left:604px}

/* page frames */
.page{position:absolute;top:0;height:900px;overflow:hidden;background:var(--white)}
.page--one{left:79px;width:482px}
.page--two{left:644px;width:552px}

.topbar{position:absolute;left:0;top:0;width:100%;background:var(--black);color:var(--white);font-size:6px;display:flex;align-items:center}
.topbar__item{display:flex;align-items:center;gap:3px;margin-right:10px}
.topbar__item svg{width:6px;height:6px}
.social{position:absolute;display:flex;gap:4px}
.social span{width:8px;height:8px;display:block}

.brand{position:absolute;display:flex;align-items:center;gap:5px}
.brand__mark{border-radius:50%;background:var(--blue)}
.brand__name{color:var(--blue);font-weight:600;white-space:nowrap}

.photo{position:absolute}
.dots{position:absolute;display:flex;gap:3px}
.dots span{width:3px;height:3px;border-radius:50%;background:var(--ink)}

.intro-title{position:absolute;font-weight:400;color:var(--ink);white-space:nowrap}
.body-copy{position:absolute;color:var(--muted);font-weight:400}

.section-title{position:absolute;width:100%;text-align:center;font-weight:400;text-transform:uppercase}
.section-sub{position:absolute;width:100%;text-align:center}

.service{position:absolute}
.service__head{display:flex;align-items:center;gap:4px;text-transform:uppercase;white-space:nowrap}
.service__text{position:absolute}

.dropdown{position:absolute;background:var(--white);border:1px solid var(--rule)}
.dropdown span{display:block;border-bottom:1px solid var(--rule);background:#f3f3f3;color:var(--soft);white-space:nowrap}
.dropdown span:last-child{border-bottom:0}

/* ---------- option one ---------- */
.page--one .topbar{height:13px;padding-left:40px}
.page--one .nav{position:absolute;left:206px;top:22px;height:15px;width:236px;background:var(--blue);display:flex;border:1px solid var(--blue-dark)}
.page--one .nav span{flex:auto;color:var(--white);font-size:5.5px;display:flex;align-items:center;justify-content:center;border-right:1px solid var(--blue-dark);white-space:nowrap}
.page--one .nav span:last-child{border-right:0}
.page--one .dropdown{left:275px;top:48px;width:48px}
.page--one .dropdown span{font-size:4.6px;line-height:11.5px;padding-left:4px}
.hero-one{left:0;top:47px;width:482px;height:165px;background:linear-gradient(90deg,#2a2522 0%,#15120f 35%,#050505 60%,#000 100%)}
.hero-one__title{position:absolute;left:281px;top:123px;color:var(--white);font-size:14px;font-weight:300;letter-spacing:.3px}
.hero-one__sub{position:absolute;left:283px;top:145px;width:160px;color:#d8d8d8;font-size:6.5px;line-height:12px}
.services-one{position:absolute;left:0;top:357px;width:482px;height:153px;background:var(--black);color:var(--white)}
.services-one .section-title{top:22px;font-size:11px}
.services-one .section-sub{top:38px;font-size:6px;color:#ddd}
.services-one .service__head{font-size:8.5px}
.services-one .service__head svg{width:13px;height:13px}
.services-one .service__text{left:22px;top:16px;width:104px;font-size:5.7px;line-height:8px;color:#ddd}
.blog-card{position:absolute;top:582px;width:91px}
.blog-card__img{height:68px}
.blog-card__title{margin-top:12px;font-size:5.7px;color:var(--ink);white-space:nowrap}
.blog-card__meta{margin-top:8px;height:11px;border-bottom:1px solid #999;display:flex;align-items:center;gap:3px;font-size:4.5px;color:var(--ink)}
.blog-card__meta i{width:8px;height:8px;background:var(--ink);display:block}
.blog-card__meta i.gap{margin-left:4px;border-radius:2px;background:#666}
.blog-card__text{margin-top:8px;font-size:5.5px;line-height:8px;color:var(--ink)}
.blog-card__btn{margin-top:5px;height:12px;background:var(--blue);color:var(--white);font-size:5.5px;display:flex;align-items:center;justify-content:center}
.footer-one{position:absolute;left:0;top:774px;width:482px;height:126px;background:var(--footer);color:var(--white)}
.footer-one__rule{position:absolute;left:48px;top:-1px;width:391px;height:3px;background:var(--black)}
.footer-one__toggle{position:absolute;left:236px;top:-10px;width:20px;height:20px;background:var(--blue);transform:rotate(45deg)}
.footer-one__arrow{position:absolute;left:240px;top:-6px;width:12px;height:12px}
.fcol{position:absolute;top:32px;font-size:4.6px;line-height:8.5px}
.fcol b{display:block;font-weight:600;margin-bottom:5px}
.footer-one__bottom{position:absolute;left:0;bottom:0;width:100%;height:14px;background:var(--black);font-size:4.5px;display:flex;align-items:center;justify-content:center;color:#ccc}

/* ---------- option two ---------- */
.page--two .topbar{height:14px;justify-content:flex-end;padding-right:6px}
.page--two .nav{position:absolute;top:30px;left:0;width:100%;font-size:6px;color:var(--soft)}
.page--two .nav span{position:absolute;white-space:nowrap}
.page--two .nav .is-active{color:var(--blue)}
.page--two .dropdown{left:330px;top:57px;width:54px}
.page--two .dropdown span{font-size:4.8px;line-height:13px;padding-left:5px}
.hero-two{left:0;top:52px;width:552px;height:190px;background:linear-gradient(90deg,#9aa3a8 0%,#d9dee0 30%,#eef1f1 55%,#c3cfd2 80%,#b08e86 100%)}
.network-art{left:356px;top:265px;width:140px;height:122px;background:linear-gradient(135deg,#f4f4f4 0%,#e4e4e4 50%,#d8dde3 100%)}
.services-two{position:absolute;left:0;top:408px;width:552px;height:175px;background:var(--band)}
.services-two .section-title{top:26px;font-size:14px;color:var(--ink)}
.services-two .section-sub{top:45px;font-size:7px;color:var(--muted)}
.services-two .service__head{font-size:11px;color:var(--ink);gap:6px}
.services-two .service__head svg{width:18px;height:18px}
.services-two .service__text{left:25px;top:22px;width:118px;font-size:6.6px;line-height:9px;color:var(--soft)}
.work-title{top:605px;font-size:13px;color:var(--ink)}
.work-sub{top:624px;font-size:7px;color:var(--muted)}
.work-img{position:absolute;top:665px;width:104px;height:79px;border:1px solid var(--rule)}
.footer-two{position:absolute;left:0;top:779px;width:552px;height:121px;background:var(--black);color:var(--white)}
.f2col{position:absolute;top:10px}
.f2col h3{font-size:11px;font-weight:400;text-transform:uppercase;letter-spacing:.2px}
.f2col ul{list-style:none;margin-top:12px;font-size:4.6px;line-height:9.3px}
.f2col li::before{content:"";display:inline-block;width:0;height:0;border-left:3px solid #fff;border-top:2px solid transparent;border-bottom:2px solid transparent;margin-right:5px}
.f2col p{margin-top:11px;font-size:4.6px;line-height:6.5px;width:95px}
.f2col .form-row{display:flex;align-items:center;font-size:4.8px;height:10px;margin-top:1px}
.f2col .form-row span{width:31px}
.f2col .form-row i{display:block;width:61px;height:7px;background:var(--white)}
.footer-two__bottom{position:absolute;left:0;bottom:0;width:100%;height:20px;border-top:1px solid #222;font-size:4.6px;display:flex;align-items:center;justify-content:center;color:#ccc}
</style>
</head>
<body>

<div class="option-label option-label--one">Design Option 1 Homepage</div>
<div class="option-label option-label--two">Design Option 2 Homepage</div>

<!-- ================= OPTION ONE ================= -->
<section class="page page--one">
  <div class="topbar">
    <span class="topbar__item"><svg viewBox="0 0 10 10"><rect x="2" y="0.5" width="6" height="9" rx="1" fill="#fff"/></svg>1(800)55501234</span>
    <span class="topbar__item"><svg viewBox="0 0 10 10"><rect x="0.5" y="2" width="9" height="6" fill="#fff"/></svg>hello@larkstone.example</span>
  </div>
  <div class="social" style="left:390px;top:2px">
    <span style="background:#3b5998"></span><span style="background:#d34836"></span><span style="background:#33a6d7"></span><span style="background:#c8232c"></span>
  </div>

  <div class="brand" style="left:41px;top:19px">
    <span class="brand__mark" style="width:19px;height:19px"></span>
    <span class="brand__name" style="font-size:9px">Larkstone Capital Partners</span>
  </div>

  <nav class="nav">
    <span>HOME</span><span>ABOUT US</span><span>SERVICES</span><span>OUR TEME</span><span>BLOG</span><span>CONTACT US</span>
  </nav>

  <div class="photo hero-one" role="img" aria-label="Portrait of a smiling banker in glasses against a dark background"></div>
  <div class="hero-one__title">INVESTMENT BANKING</div>
  <p class="hero-one__sub">Our sector experts and transactional specialists partner to help clients</p>

  <div class="dropdown"><span>SERVICES PAGE 1</span><span>SERVICES PAGE 2</span><span>SERVICES PAGE 3</span></div>

  <div class="dots" style="left:233px;top:221px"><span></span><span></span><span></span></div>

  <h2 class="intro-title" style="left:40px;top:247px;font-size:11.5px">Created to promote your business</h2>
  <p class="body-copy" style="left:40px;top:271px;width:230px;font-size:6px;line-height:12.2px">Lorem ipsum dolor sit amet, consectetur adipiscing elit. Nullam condimentum leo felis, ut aliquet nisi lobortis ac. Nulla ipsum erat, mollis sit amet est sed, commodo accumsan magna. Morbi a lectus rhoncus odio sollicitudin rhoncus dictum vel turpis. Curabitur luctus lobortis hendrerit</p>
  <div class="photo" style="left:322px;top:249px;width:120px;height:75px;background:linear-gradient(160deg,#7fb2e6 0%,#3f79c0 45%,#2a5e9e 75%,#5b8a46 100%)" role="img" aria-label="Glass office tower under a blue sky"></div>

  <div class="services-one">
    <h2 class="section-title">Our Services</h2>
    <p class="section-sub">For further details on our existing projects see the Projects section.</p>
    <div class="service" style="left:41px;top:80px">
      <div class="service__head"><svg viewBox="0 0 14 14"><path d="M3 6V4a3 3 0 0 1 6 0" fill="none" stroke="#fff" stroke-width="1.4"/><rect x="1" y="6" width="10" height="7" fill="#fff"/></svg>ONLINE BANKING</div>
      <p class="service__text">Ventrix offers a secure and reliable banking/payment platform, which can easily be customized according to your requirements.</p>
    </div>
    <div class="service" style="left:178px;top:80px">
      <div class="service__head"><svg viewBox="0 0 14 14"><rect x="3.5" y="0.5" width="7" height="13" rx="1" fill="none" stroke="#fff" stroke-width="1.2"/><circle cx="7" cy="11.3" r=".8" fill="#fff"/></svg>MOBILE BANKING</div>
      <p class="service__text">Ventrix offers a secure and reliable banking/payment platform, which can easily be customized according to your requirements.</p>
    </div>
    <div class="service" style="left:317px;top:80px">
      <div class="service__head"><svg viewBox="0 0 14 14"><rect x="5" y="1.5" width="4" height="2.5" fill="none" stroke="#fff"/><rect x="1" y="4" width="12" height="8.5" fill="#fff"/><rect x="6" y="7" width="2" height="2" fill="#000"/></svg>MARKETPLACE</div>
      <p class="service__text">Ventrix offers a secure and reliable banking/payment platform, which can easily be customized according to your requirements.</p>
    </div>
  </div>

  <h2 class="section-title" style="top:529px;font-size:12px;color:var(--ink)">Blog</h2>
  <p class="section-sub" style="top:546px;font-size:6px;color:var(--ink)">For further details on our existing projects see the Projects section.</p>

  <article class="blog-card" style="left:40px">
    <div class="blog-card__img" style="background:linear-gradient(135deg,#e8eef5 0%,#3a64b4 45%,#1f3f86 70%,#c9d3de 100%)" role="img" aria-label="Office tower facade seen from below"></div>
    <div class="blog-card__title">BEST PROJECT OF THIS THEME</div>
    <div class="blog-card__meta"><i></i>September 16, 2013<i class="gap"></i>(15)</div>
    <p class="blog-card__text">Lorem ipsum dolor sit amet, consectetur adipis, consectetur</p>
    <div class="blog-card__btn">VIEW DETAILS</div>
  </article>
  <article class="blog-card" style="left:144px">
    <div class="blog-card__img" style="background:linear-gradient(180deg,#9fc0da 0%,#cfdde6 40%,#7a5a42 75%,#3c2c22 100%)" role="img" aria-label="Boardroom with a long conference table"></div>
    <div class="blog-card__title">BEST PROJECT OF THIS THEME</div>
    <div class="blog-card__meta"><i></i>September 16, 2013<i class="gap"></i>(15)</div>
    <p class="blog-card__text">Lorem ipsum dolor sit amet, consectetur adipis, consectetur</p>
    <div class="blog-card__btn">VIEW DETAILS</div>
  </article>
  <article class="blog-card" style="left:248px">
    <div class="blog-card__img" style="background:linear-gradient(135deg,#e8eef5 0%,#3a64b4 45%,#1f3f86 70%,#c9d3de 100%)" role="img" aria-label="Office tower facade seen from below"></div>
    <div class="blog-card__title">BEST PROJECT OF THIS THEME</div>
    <div class="blog-card__meta"><i></i>September 16, 2013<i class="gap"></i>(15)</div>
    <p class="blog-card__text">Lorem ipsum dolor sit amet, consectetur adipis, consectetur</p>
    <div class="blog-card__btn">VIEW DETAILS</div>
  </article>
  <article class="blog-card" style="left:352px">
    <div class="blog-card__img" style="background:linear-gradient(180deg,#9fc0da 0%,#cfdde6 40%,#7a5a42 75%,#3c2c22 100%)" role="img" aria-label="Boardroom with a long conference table"></div>
    <div class="blog-card__title">BEST PROJECT OF THIS THEME</div>
    <div class="blog-card__meta"><i></i>September 16, 2013<i class="gap"></i>(15)</div>
    <p class="blog-card__text">Lorem ipsum dolor sit amet, consectetur adipis, consectetur</p>
    <div class="blog-card__btn">VIEW DETAILS</div>
  </article>

  <footer class="footer-one">
    <div class="footer-one__rule"></div>
    <div class="footer-one__toggle"></div>
    <svg class="footer-one__arrow" viewBox="0 0 12 12"><path d="M3 8 L6 5 L9 8" fill="none" stroke="#fff" stroke-width="1.3"/></svg>
    <div class="fcol" style="left:55px;width:88px"><b>ABOUT TOVREN GOODS</b>By subscribing to our mailing list you will always be update with the latest news from us. By subscribing to our mailing list you will always be update with the latest news from us.</div>
    <div class="fcol" style="left:155px"><b>MEN'S ACCESSORIES</b>SUN GLASSES<br>HATS &amp; CAPS<br>WALLETS<br>WATCHES</div>
    <div class="fcol" style="left:222px"><b>WOMEN ACCESSORIES</b>SUN GLASSES<br>HATS &amp; CAPS<br>WALLETS<br>WATCHES</div>
    <div class="fcol" style="left:289px"><b>NEW ARRIVALS</b>SUN GLASSES<br>HATS &amp; CAPS<br>WALLETS<br>WATCHES</div>
    <div class="fcol" style="left:356px"><b>CONTACT US</b>T (555) 010-2233<br>Email: sales@tovren.example<br><br>Your Company LTD<br>Orchard Lane 12, 90210, Westfall</div>
    <div class="footer-one__bottom">© 2014 Larkstone - All Rights Reserved</div>
  </footer>
</section>

<!-- ================= OPTION TWO ================= -->
<section class="page page--two">
  <div class="topbar">
    <span class="topbar__item"><svg viewBox="0 0 10 10"><rect x="2" y="0.5" width="6" height="9" rx="1" fill="#fff"/></svg>1(800)55501234</span>
    <span class="topbar__item" style="margin-right:0"><svg viewBox="0 0 10 10"><rect x="0.5" y="2" width="9" height="6" fill="#fff"/></svg>hello@larkstone.example</span>
  </div>

  <div class="brand" style="left:46px;top:21px">
    <span class="brand__mark" style="width:22px;height:22px"></span>
    <span class="brand__name" style="font-size:10.5px">Larkstone Capital Partners</span>
  </div>

  <nav class="nav">
    <span style="left:252px">HOME</span>
    <span style="left:298px">ABOUT US</span>
    <span style="left:344px" class="is-active">SERVICES</span>
    <span style="left:388px">OUR TEME</span>
    <span style="left:435px">BLOGE</span>
    <span style="left:470px">CONTACT US</span>
  </nav>

  <div class="photo hero-two" role="img" aria-label="Team of four business professionals standing by an office window"></div>

  <div class="dropdown"><span>SERVICES PAGE 1</span><span>SERVICES PAGE 2</span><span>SERVICES PAGE 3</span></div>

  <div class="dots" style="left:266px;top:252px"><span></span><span></span><span></span></div>

  <h2 class="intro-title" style="left:46px;top:283px;font-size:13px">Created to promote your business</h2>
  <p class="body-copy" style="left:46px;top:310px;width:262px;font-size:7px;line-height:14.2px">Lorem ipsum dolor sit amet, consectetur adipiscing elit. Nullam condimentum leo felis, ut aliquet nisi lobortis ac. Nulla ipsum erat, mollis sit amet est sed, commodo accumsan magna. Morbi a lectus rhoncus odio sollicitudin rhoncus dictum vel turpis. Curabitur luctus lobortis hendrerit</p>
  <div class="photo network-art" role="img" aria-label="Illustration of a connected network graphic"></div>

  <div class="services-two">
    <h2 class="section-title">Our Services</h2>
    <p class="section-sub">For further details on our existing projects see the Projects section.</p>
    <div class="service" style="left:46px;top:88px">
      <div class="service__head"><svg viewBox="0 0 14 14"><path d="M3 6V4a3 3 0 0 1 6 0" fill="none" stroke="#333" stroke-width="1.4"/><rect x="1" y="6" width="10" height="7" fill="#333"/></svg>ONLINE BANKING</div>
      <p class="service__text">Ventrix offers a secure and reliable banking/payment platform, which can easily be customized according to your requirements.</p>
    </div>
    <div class="service" style="left:203px;top:88px">
      <div class="service__head"><svg viewBox="0 0 14 14"><rect x="3.5" y="0.5" width="7" height="13" rx="1" fill="none" stroke="#333" stroke-width="1.2"/><circle cx="7" cy="11.3" r=".8" fill="#333"/></svg>MOBILE BANKING</div>
      <p class="service__text">Ventrix offers a secure and reliable banking/payment platform, which can easily be customized according to your requirements.</p>
    </div>
    <div class="service" style="left:362px;top:88px">
      <div class="service__head"><svg viewBox="0 0 14 14"><rect x="5" y="1.5" width="4" height="2.5" fill="none" stroke="#333"/><rect x="1" y="4" width="12" height="8.5" fill="#333"/><rect x="6" y="7" width="2" height="2" fill="#efefef"/></svg>MARKETPLACE</div>
      <p class="service__text">Ventrix offers a secure and reliable banking/payment platform, which can easily be customized according to your requirements.</p>
    </div>
  </div>

  <h2 class="section-title work-title">Our Work</h2>
  <p class="section-sub work-sub">For further details on our existing projects see the Projects section.</p>
  <div class="work-img" style="left:46px;background:linear-gradient(135deg,#e8eef5 0%,#3a64b4 45%,#1f3f86 70%,#c9d3de 100%)" role="img" aria-label="Office tower facade seen from below"></div>
  <div class="work-img" style="left:165px;background:linear-gradient(180deg,#9fc0da 0%,#cfdde6 40%,#7a5a42 75%,#3c2c22 100%)" role="img" aria-label="Boardroom with a long conference table"></div>
  <div class="work-img" style="left:284px;background:linear-gradient(135deg,#e8eef5 0%,#3a64b4 45%,#1f3f86 70%,#c9d3de 100%)" role="img" aria-label="Office tower facade seen from below"></div>
  <div class="work-img" style="left:403px;background:linear-gradient(180deg,#9fc0da 0%,#cfdde6 40%,#7a5a42 75%,#3c2c22 100%)" role="img" aria-label="Boardroom with a long conference table"></div>

  <footer class="footer-two">
    <div class="f2col" style="left:46px">
      <h3>Profile</h3>
      <ul><li>Partners</li><li>Nexal Team</li><li>Why Nexal?</li><li>Work Approach</li><li>Methodology</li><li>Client Communication</li></ul>
    </div>
    <div class="f2col" style="left:165px">
      <h3>Services</h3>
      <p>Lorem Ipsum is simply dummy text of the printing and typesetting industry. Lorem Ipsum has been the industry's standard text ever since the 1500s.</p>
      <ul style="margin-top:6px"><li>Lorem Ipsum is simply dummy text</li><li>Lorem Ipsum is simply dummy text</li><li>Lorem Ipsum is simply dummy text</li></ul>
    </div>
    <div class="f2col" style="left:284px">
      <h3>Technologies</h3>
      <ul><li>Cloud Technologies</li><li>PHP/MYSQL</li><li>Open Source</li><li>Mobile Application Development</li><li>Web Design and Graphic Design</li><li>Team Portal Suite</li></ul>
    </div>
    <div class="f2col" style="left:402px">
      <h3>Contact Us</h3>
      <p>Lorem Ipsum is simply dummy text of the printing and typesetting industry. Lorem Ipsum as been the industry</p>
      <div style="margin-top:6px">
        <div class="form-row"><span>Name</span><i></i></div>
        <div class="form-row"><span>Email addres</span><i></i></div>
        <div class="form-row"><span>Phone No</span><i></i></div>
      </div>
    </div>
    <div class="footer-two__bottom">Copyright @ 2014. company (Brightmoor)</div>
  </footer>
</section>

</body>
</html>
```